Business card design for Plumbing and Gas fitting company

We need a business card design for our plumbing and gas fitting company using the company logo and director details. Design should be modern and eye-catching however kept reasonably simple. This design should be targeted at commercial businesses/work so professionalism is key.

Target Market(s)

Commercial/business

Industry/Entity Type

Plumbing

Contact Information for Business Card

Warwick Tane
Director
027 815 0937
warwick@harbourlinepipeworks.example
PO Box 8716
Ashgrove Vale 7390

Font styles to use
Sans Serif

Requirements
Must have
• Logo
• Modern
• Kept simple
Nice to have
• Colour scheme based around logo

```html
<!DOCTYPE html>
<html lang="en">
<head>
<meta charset="utf-8">
<title>Harbourline Pipeworks – Business Card</title>
<link href="https://fonts.googleapis.com/css2?family=Open+Sans:wght@300;400;600;700&display=swap" rel="stylesheet">
<style>
  :root {
    --backdrop: #5d6a73;
    --card: #050505;
    --brand-blue: #1a78c8;
    --brand-orange: #e8772e;
    --pipe-grey: #7d7d7d;
    --text-white: #f4f4f4;
    --text-grey: #9a9a9a;
  }
  * { margin: 0; padding: 0; box-sizing: border-box; }
  html, body {
    width: 1200px;
    height: 900px;
    overflow: hidden;
  }
  body {
    background: var(--backdrop);
    font-family: "Open Sans", Arial, sans-serif;
    position: relative;
  }
  .card {
    position: absolute;
    left: 250px;
    width: 700px;
    height: 400px;
    background: var(--card);
    border-radius: 4px;
    box-shadow: 0 14px 30px rgba(0,0,0,0.45);
    overflow: hidden;
  }
  .card--front { top: 40px; }
  .card--back { top: 460px; }

  .brand {
    display: flex;
    align-items: center;
    gap: 14px;
  }
  .brand__dot {
    border-radius: 50%;
    background: var(--brand-orange);
    flex: none;
  }
  .brand__name {
    color: var(--brand-blue);
    font-weight: 700;
    white-space: nowrap;
  }

  .card--front .brand {
    position: absolute;
    left: 0; right: 0;
    top: 50%;
    transform: translateY(-50%);
    justify-content: center;
  }
  .card--front .brand__name { font-size: 44px; }
  .card--front .brand__dot { width: 40px; height: 40px; }

  .pipe-tab {
    position: absolute;
    width: 22px;
    height: 100px;
    background: var(--pipe-grey);
  }
  .pipe-tab--left { left: 0; top: 40px; border-radius: 0 8px 8px 0; }
  .pipe-tab--right { right: 0; bottom: 40px; border-radius: 8px 0 0 8px; }

  .card--back .brand {
    position: absolute;
    left: 150px;
    top: 40px;
  }
  .card--back .brand__name { font-size: 24px; }
  .card--back .brand__dot { width: 22px; height: 22px; }

  .contact {
    position: absolute;
    left: 70px;
    top: 118px;
  }
  .contact__name {
    color: var(--text-white);
    font-size: 24px;
    font-weight: 600;
    margin-left: 18px;
  }
  .contact__role {
    color: var(--text-grey);
    font-size: 12px;
    font-weight: 400;
    margin-top: -2px;
  }
  .contact__list {
    list-style: none;
    margin-top: 12px;
  }
  .contact__item {
    display: flex;
    align-items: center;
    gap: 8px;
    color: var(--text-grey);
    font-size: 13px;
    font-weight: 300;
    line-height: 22px;
  }
  .contact__item svg { width: 12px; height: 12px; fill: var(--text-white); flex: none; }

  .divider {
    position: absolute;
    left: 70px;
    right: 60px;
    top: 250px;
    height: 2px;
    background: var(--brand-blue);
  }
  .address {
    position: absolute;
    right: 60px;
    top: 268px;
    text-align: right;
    color: var(--text-grey);
    font-size: 15px;
    font-weight: 400;
    line-height: 22px;
    font-style: normal;
  }
</style>
</head>
<body>

  <section class="card card--front" aria-label="Card front">
    <span class="pipe-tab pipe-tab--left"></span>
    <div class="brand">
      <span class="brand__name">Harbourline Pipeworks</span>
      <span class="brand__dot"></span>
    </div>
    <span class="pipe-tab pipe-tab--right"></span>
  </section>

  <section class="card card--back" aria-label="Card back">
    <div class="brand">
      <span class="brand__name">Harbourline Pipeworks</span>
      <span class="brand__dot"></span>
    </div>

    <div class="contact">
      <h1 class="contact__name">Warwick Tane</h1>
      <p class="contact__role">Director</p>
      <ul class="contact__list">
        <li class="contact__item">
          <svg viewBox="0 0 24 24" aria-hidden="true"><path d="M6.6 10.8a15.1 15.1 0 0 0 6.6 6.6l2.2-2.2a1 1 0 0 1 1-.25 11.4 11.4 0 0 0 3.6.57 1 1 0 0 1 1 1V20a1 1 0 0 1-1 1A17 17 0 0 1 3 4a1 1 0 0 1 1-1h3.5a1 1 0 0 1 1 1c0 1.25.2 2.450.57 3.57a1 1 0 0 1-.25 1z"/></svg>
          027 815 0937
        </li>
        <li class="contact__item">
          <svg viewBox="0 0 24 24" aria-hidden="true"><path d="M2 5h20v14H2z M4 7v.5l8 5 8-5V7l-8 5z" fill-rule="evenodd"/></svg>
          warwick@harbourlinepipeworks.example
        </li>
      </ul>
    </div>

    <div class="divider"></div>

    <address class="address">
      PO Box 8716<br>
      Ashgrove Vale 7390
    </address>
  </section>

</body>
</html>
```